Vision Mission Values Layout for Displaying

We our looking for a format or template that we can transfer onto canvas, metal, or picture to display in our front lobby, break room, and conference room. We would like to incorporate our company logo and colors. Red Black & White. We would like them all displayed on the same canvas, sheet metal, or picture. This is our first time using this site we are hoping to use this site for our web design and possible re design our logo. When we walk into other businesses we see their vision, mission, and values displayed. We are looking for something similar.

Industry/Entity Type

It Company

Requirements
Must have
• Company Name and Logo
• Mission Vision and Values
Nice to have
• the definitions
Should not have
• Contact Information

```html
<!DOCTYPE html>
<html lang="en">
<head>
<meta charset="UTF-8">
<title>Norvane Fabrication – Vision, Mission &amp; Values</title>
<link rel="stylesheet" href="https://fonts.googleapis.com/css2?family=Source+Sans+3:ital,wght@0,400;0,600;0,700;1,600;1,700&display=swap">
<style>
  :root {
    --page-bg: #e6e8e4;
    --brand-red: #e31b23;
    --brand-red-dark: #b8121a;
    --brand-red-deep: #8f0d13;
    --brand-black: #1d1d1d;
    --brand-grey-light: #c9c9c9;
    --accent-pink: #f39a9d;
    --paper-white: #ffffff;
    --text-on-red: #ffffff;
  }
  * { box-sizing: border-box; margin: 0; padding: 0; }
  html, body {
    width: 1200px;
    height: 848px;
    overflow: hidden;
    background: var(--page-bg);
    font-family: "Source Sans 3", "Myriad Pro", Arial, sans-serif;
  }
  .poster {
    position: absolute;
    left: 317px;
    top: 24px;
    width: 566px;
    height: 800px;
    background: var(--paper-white);
    box-shadow: 0 6px 20px rgba(0,0,0,0.18);
    overflow: hidden;
  }
  .poster__backdrop {
    position: absolute;
    inset: 0;
    width: 100%;
    height: 100%;
  }
  .poster__accent {
    position: absolute;
    left: 350px;
    top: 18px;
    width: 150px;
    height: 92px;
    background: linear-gradient(135deg, var(--brand-black) 0%, #4a1a1c 55%, var(--accent-pink) 100%);
    opacity: 0.9;
  }
  .poster__content {
    position: absolute;
    left: 44px;
    top: 58px;
    width: 350px;
    color: var(--text-on-red);
  }
  .statement { margin-bottom: 20px; }
  .statement__title {
    font-size: 27px;
    font-weight: 600;
    line-height: 1.05;
    letter-spacing: -0.2px;
  }
  .statement__text {
    font-size: 14px;
    line-height: 1.3;
    margin-top: 3px;
  }
  .statement--vision .statement__text { font-size: 13px; }
  .values__title {
    font-size: 30px;
    font-weight: 600;
    line-height: 1.1;
    margin-top: 30px;
    margin-bottom: 4px;
  }
  .value {
    font-size: 14px;
    line-height: 1.32;
    margin-bottom: 10px;
  }
  .value__name {
    font-weight: 700;
    font-style: italic;
  }
  .brand {
    position: absolute;
    right: 40px;
    bottom: 120px;
    display: flex;
    align-items: center;
    gap: 10px;
  }
  .brand__square {
    width: 18px;
    height: 18px;
    background: var(--brand-red);
  }
  .brand__name {
    font-size: 24px;
    font-weight: 700;
    line-height: 1;
    color: var(--brand-black);
    text-transform: uppercase;
  }
</style>
</head>
<body>
  <main class="poster">
    <svg class="poster__backdrop" viewBox="0 0 566 800" preserveAspectRatio="none" aria-hidden="true">
      <defs>
        <linearGradient id="redField" x1="0" y1="0" x2="1" y2="1">
          <stop offset="0" stop-color="#ea2129"/>
          <stop offset="0.6" stop-color="#e31b23"/>
          <stop offset="1" stop-color="#c5151c"/>
        </linearGradient>
        <linearGradient id="greyWedge" x1="0" y1="0" x2="1" y2="0">
          <stop offset="0" stop-color="#3d3d3d"/>
          <stop offset="1" stop-color="#7a7a7a"/>
        </linearGradient>
      </defs>
      <polygon points="0,0 566,0 566,560 0,760" fill="url(#redField)"/>
      <polygon points="300,200 566,150 566,330" fill="var(--brand-red-dark)" opacity="0.35"/>
      <polygon points="430,330 566,300 566,420" fill="var(--brand-red-deep)" opacity="0.35"/>
      <polygon points="0,560 240,700 0,760" fill="var(--brand-red-dark)" opacity="0.4"/>
      <polygon points="200,540 566,470 566,560" fill="var(--brand-red-dark)" opacity="0.25"/>
      <polygon points="0,800 0,770 250,705 420,800" fill="url(#greyWedge)"/>
      <polygon points="250,705 300,680 420,800" fill="var(--brand-grey-light)" opacity="0.6"/>
    </svg>

    <div class="poster__accent" role="img" aria-label="Decorative angular accent in black and pink"></div>

    <section class="poster__content">
      <div class="statement statement--vision">
        <h2 class="statement__title">Vision Statement:</h2>
        <p class="statement__text">Exceptional People Fabricating Inspiring Projects</p>
      </div>
      <div class="statement">
        <h2 class="statement__title">Mission Statement:</h2>
        <p class="statement__text">Our Mission is to be the “Steel Fabricator of Choice” through innovative solutions and the consistent delivery of a high quality customer experience!</p>
      </div>

      <h2 class="values__title">Values:</h2>
      <p class="value"><span class="value__name">Integrity:</span> Consistency, Fairness, Commitment, Ethical, Moral, Do What We Say We Are Going to Do, Do the Right Thing Always</p>
      <p class="value"><span class="value__name">Excellence:</span> High Quality, Drive, Talent, Best, the Gold Standard, Being your Best</p>
      <p class="value"><span class="value__name">Passion:</span> Driven, Spirited, Enthusiasm, Competitive, Enjoyment, Energy</p>
      <p class="value"><span class="value__name">Customer-Focused:</span> Exceeding Requirements, Communication, Passion to Serve, Understanding of Customer’s Needs, Solutions-Oriented, Dedicated to the Success of Others, Responsive, Sense of Urgency</p>
      <p class="value"><span class="value__name">Collaboration:</span> Teamwork, Engagement, Partnership, Relationship, Listening, Communication, Sharing, Collective, Community</p>
      <p class="value"><span class="value__name">Innovation:</span> Creativity, Cutting-Edge, Smart, LEAN, Leading, Performance, Continuous Improvement</p>
    </section>

    <div class="brand">
      <span class="brand__square"></span>
      <span class="brand__name">Norvane<br>Fabrication</span>
    </div>
  </main>
</body>
</html>
```